Brantley Advisory Group provides support for renewable energy projects to utilities and suppliers

I need a professional looking business card that is both simple and elegant and unique. My clients are mostly large organizations not individuals. I am a consultant with my own company that is small but would like to give clients the impression I am larger. Smart grid, fiber optics, software, field hardware, distribution automation, substation automation, operations, energy storage/batteries, microgrids, customer service, strategy/roadmaps, conservation, Automated Metering Infrastruture (AMI or smart meters) are all areas of focus.

Target Market(s)

Utilities, suppliers, governmental agencies involved in energy. All types of energy especially natural gas and electrical. Especially renewable energy or green projects.

Contact Information for Business Card

Name - Mark Brantley Cell Phone - 425.318.2746 Email - mbrantley@brantleyag-example.com
Company - Brantley Advisory Group (logo) Title - Principal

Font styles to use
Serif
Sans Serif

Colors

Designer to choose colors to be used in the design.

Requirements
Must have
• Simple and professional and powerful.
• Unique/creative design.
Nice to have
• Utilize color scheme to accent logo colors. Maybe some geometric pattern on edge of card with color.
Should not have
• Busy, complicated, traditional

```html
<!DOCTYPE html>
<html lang="en">
<head>
<meta charset="utf-8">
<title>Brantley Advisory Group – Business Card</title>
<link rel="stylesheet" href="https://fonts.googleapis.com/css2?family=Montserrat:wght@400;500;700&display=swap">
<style>
  :root {
    --backdrop: #e9e7e3;
    --card: #ffffff;
    --brand-blue: #2626a3;
    --brand-green: #6a9a4f;
    --shadow: rgba(0, 0, 0, 0.18);
  }
  html, body {
    margin: 0;
    width: 1200px;
    height: 800px;
    overflow: hidden;
    background: var(--backdrop);
    font-family: "Montserrat", Arial, sans-serif;
  }
  .canvas {
    position: relative;
    width: 1200px;
    height: 800px;
  }
  .business-card {
    position: absolute;
    left: 180px;
    top: 160px;
    width: 840px;
    height: 480px;
    background: var(--card);
    box-shadow: 0 14px 40px var(--shadow);
    overflow: hidden;
  }
  .edge-accent {
    position: absolute;
    right: 0;
    width: 14px;
  }
  .edge-accent--blue {
    top: 0;
    height: 120px;
    background: var(--brand-blue);
  }
  .edge-accent--green {
    top: 150px;
    height: 52px;
    background: var(--brand-green);
  }
  .brand {
    position: absolute;
    left: 64px;
    top: 62px;
    display: flex;
    align-items: center;
    gap: 18px;
  }
  .brand-square {
    width: 34px;
    height: 34px;
    border: 4px solid var(--brand-green);
    border-radius: 5px;
    box-sizing: border-box;
  }
  .brand-name {
    margin: 0;
    font-size: 32px;
    font-weight: 700;
    color: var(--brand-blue);
    letter-spacing: 0.5px;
  }
  .person {
    position: absolute;
    left: 64px;
    top: 190px;
  }
  .person-name {
    margin: 0;
    font-size: 50px;
    font-weight: 400;
    text-transform: uppercase;
    color: var(--brand-blue);
    letter-spacing: 1px;
    line-height: 1;
  }
  .person-title {
    margin: 12px 0 0 4px;
    font-size: 15px;
    font-weight: 500;
    text-transform: uppercase;
    letter-spacing: 4px;
    color: var(--brand-green);
  }
  .contact-list {
    list-style: none;
    margin: 34px 0 0 0;
    padding: 0;
  }
  .contact-item {
    display: flex;
    align-items: center;
    gap: 14px;
    font-size: 24px;
    font-weight: 500;
    color: var(--brand-blue);
    margin-bottom: 12px;
  }
  .contact-icon {
    width: 22px;
    height: 22px;
    flex: none;
  }
</style>
</head>
<body>
<main class="canvas">
  <article class="business-card">
    <span class="edge-accent edge-accent--blue"></span>
    <span class="edge-accent edge-accent--green"></span>

    <header class="brand">
      <span class="brand-square" aria-hidden="true"></span>
      <h1 class="brand-name">Brantley Advisory Group</h1>
    </header>

    <section class="person">
      <h2 class="person-name">Mark Brantley</h2>
      <p class="person-title">Principal</p>
      <ul class="contact-list">
        <li class="contact-item">
          <svg class="contact-icon" viewBox="0 0 22 22" aria-hidden="true">
            <rect x="5" y="1.5" width="12" height="19" rx="2" fill="none" stroke="#6a9a4f" stroke-width="2"/>
            <line x1="9" y1="17" x2="13" y2="17" stroke="#6a9a4f" stroke-width="2"/>
          </svg>
          <span>425.318.2746</span>
        </li>
        <li class="contact-item">
          <svg class="contact-icon" viewBox="0 0 22 22" aria-hidden="true">
            <rect x="1.5" y="4.5" width="19" height="13" fill="none" stroke="#6a9a4f" stroke-width="2"/>
            <polyline points="1.5,4.5 11,12 20.5,4.5" fill="none" stroke="#6a9a4f" stroke-width="2"/>
          </svg>
          <span>mbrantley@brantleyag-example.com</span>
        </li>
      </ul>
    </section>
  </article>
</main>
</body>
</html>
```